The Brisk Hound - Dog Training Business Card Design

I need a business card design for a new dog training company based in Cronulla NSW called The Brisk Hound. I run puppy pre school classes, adult dog classes and do one on one training in the person's home.
I have studied for 2 years and use positive reinforcement training methods based on how dogs learn. I believe in communicating with our dogs what we want them to do rather than punish them for behaviours we don't like. I would like to see designs that use the colours that are used in my logo (please see attached)
I would like a simple and classic looking design. I don't want cartoon images of dogs or any animal images or drawings on the card. I have created my logo with this mindset. I am open to the subtle use of a dog's tail, paws or paw print.

Target Market(s)

high end area which is why I want a classic looking design
adults aged 25 and over

Industry/Entity Type

Dog Training

Contact Information for Business Card

Marisa Tolland
KOBRA Trained Professional Dog Trainer
www.thebriskhound-example.com.au
0437582061
marisa@thebriskhound-example.com.au

Font styles to use
Sans Serif

Colors
ffffff
86cae6
757575

Requirements
Must have
• Logo - I am trying to attach my logo and colour palette but it won't allow me. I will contact the company and upload ASAP.
Should not have
• images of dogs or cartoon drawings

```html
<!DOCTYPE html>
<html lang="en">
<head>
<meta charset="utf-8">
<title>The Brisk Hound – Business Card</title>
<link rel="stylesheet" href="https://fonts.googleapis.com/css2?family=Noto+Serif:wght@400&family=Pinyon+Script&display=swap">
<style>
  :root {
    --stage: #e8e5e0;
    --white: #ffffff;
    --card-white: #fbfbfb;
    --blue: #86cae6;
    --grey: #757575;
    --grey-dark: #5f5f5f;
    --grey-light: #8a8a8a;
    --ink: #111111;
    --text: #4a4a4a;
    --pattern: #f1f1f1;
  }
  html, body {
    margin: 0;
    padding: 0;
    width: 1108px;
    height: 1200px;
    overflow: hidden;
    background: var(--stage);
  }
  .canvas {
    position: relative;
    width: 1108px;
    height: 1200px;
  }
  .card {
    position: absolute;
    top: 210px;
    width: 470px;
    height: 780px;
    border-radius: 24px;
    overflow: hidden;
    box-shadow: 0 8px 22px rgba(0,0,0,0.18);
  }
  .card--back {
    left: 54px;
    background: radial-gradient(ellipse at 50% 45%, var(--grey-light) 0%, var(--grey) 55%, var(--grey-dark) 100%);
  }
  .card--front {
    left: 584px;
    background: var(--card-white);
    font-family: "Noto Serif", serif;
  }
  .paw-pattern {
    position: absolute;
    inset: 0;
    background: linear-gradient(180deg, var(--pattern) 0%, var(--card-white) 60%, var(--pattern) 100%);
  }
  .brand-ring {
    position: absolute;
    left: 50%;
    top: 50%;
    width: 338px;
    height: 338px;
    margin: -169px 0 0 -169px;
    border: 5px solid var(--white);
    border-radius: 50%;
    box-sizing: border-box;
    display: flex;
    align-items: center;
    justify-content: center;
  }
  .brand-disc {
    position: absolute;
    left: 50%;
    top: 52px;
    width: 330px;
    height: 330px;
    margin-left: -165px;
    border-radius: 50%;
    background: var(--grey);
    display: flex;
    align-items: center;
    justify-content: center;
  }
  .brand-name {
    margin: 0;
    font-family: "Noto Serif", serif;
    font-weight: 400;
    font-size: 46px;
    line-height: 1.1;
    color: var(--white);
    text-align: center;
  }
  .contact {
    position: absolute;
    left: 0;
    right: 0;
    top: 420px;
    text-align: center;
  }
  .person-name {
    margin: 0;
    font-family: "Pinyon Script", cursive;
    font-weight: 400;
    font-size: 56px;
    line-height: 1;
    color: var(--ink);
  }
  .person-role {
    margin: 8px 0 0;
    font-size: 25px;
    line-height: 1.3;
    color: var(--text);
  }
  .divider {
    display: block;
    margin: 20px auto 0;
  }
  .phone {
    margin: 14px 0 0;
    font-size: 50px;
    letter-spacing: 2px;
    color: var(--blue);
  }
  .details {
    list-style: none;
    margin: 8px 0 0;
    padding: 0 0 0 44px;
    text-align: left;
  }
  .details li {
    display: flex;
    align-items: center;
    gap: 10px;
    font-size: 18.5px;
    line-height: 1.55;
    color: var(--text);
  }
  .details svg { flex: none; }
</style>
</head>
<body>
<main class="canvas">

  <section class="card card--back" aria-label="Card back">
    <div class="brand-ring">
      <p class="brand-name">The<br>Brisk<br>Hound</p>
    </div>
  </section>

  <section class="card card--front" aria-label="Card front">
    <div class="paw-pattern" role="img" aria-label="Faint paw print pattern across the card"></div>
    <div class="brand-disc">
      <p class="brand-name">The<br>Brisk<br>Hound</p>
    </div>
    <div class="contact">
      <h1 class="person-name">Marisa Tolland</h1>
      <p class="person-role">KOBRA Trained<br>Professional Dog Trainer</p>
      <svg class="divider" width="340" height="10" viewBox="0 0 340 10" aria-hidden="true">
        <line x1="4" y1="5" x2="336" y2="5" stroke="#333" stroke-width="1.2"/>
        <circle cx="4" cy="5" r="2.5" fill="#333"/>
        <circle cx="336" cy="5" r="2.5" fill="#333"/>
        <circle cx="170" cy="5" r="4" fill="#333"/>
      </svg>
      <p class="phone">0437582061</p>
      <ul class="details">
        <li>
          <svg width="20" height="14" viewBox="0 0 20 14" aria-hidden="true">
            <rect x="1" y="1" width="18" height="12" fill="none" stroke="#555" stroke-width="1.6"/>
            <polyline points="1,1 10,8 19,1" fill="none" stroke="#555" stroke-width="1.6"/>
          </svg>
          marisa@thebriskhound-example.com.au
        </li>
        <li>
          <svg width="20" height="20" viewBox="0 0 20 20" aria-hidden="true">
            <circle cx="10" cy="10" r="8.5" fill="none" stroke="#555" stroke-width="1.5"/>
            <ellipse cx="10" cy="10" rx="4" ry="8.5" fill="none" stroke="#555" stroke-width="1.2"/>
            <line x1="1.5" y1="10" x2="18.5" y2="10" stroke="#555" stroke-width="1.2"/>
          </svg>
          www.thebriskhound-example.com.au
        </li>
      </ul>
    </div>
  </section>

</main>
</body>
</html>
```